Design range of flavoured vodka soda cans

We need help designing a range of flavoured vodka soda cans.
Our company is www.carrowbeacon.com.au
Vodka soda flavours include;
- Raspberry
- Grape
- Blueberry
- Pina Colada
- Musk
- Lime
- Pineapple
- Watermelon
- Tropical Punch
- Honeycomb
- Pineapple and Lime

Plus separately a cocktail range including;
- Berry Fizzle
- Espresso Martini
- Candywheel
- Swirlo
- Passionfruit Gin and Tonic
- Signature Gin and Tonic

Can specifications attached

3.5% ALC/VOL
250ml Cans

Target Market(s)

25-35 Mainly Female

Industry/Entity Type

Alcoholic Beverages

Requirements
Must have
• Clear logo, room for a barcode to be added, 250ml and 3.5% ALC/VOL on the front centre, Australian pregnancy warning logo see attachments, 0.79 standard drink logo, simple description, "Produced By: Carrow Beacon Pty Ltd 9/22 Tamblin Crescent Edgeworth NSW 2285"
Nice to have
• Simple consistent design for the range, fresh look, vibrant
Should not have
• Cartoon characters or anything perceived to be attractive to minors

```html
<!DOCTYPE html>
<html lang="en">
<head>
<meta charset="utf-8">
<title>Carrow Beacon Raspberry Vodka Soda Can Label</title>
<link href="https://fonts.googleapis.com/css2?family=Poppins:wght@400;500&family=Sacramento&display=swap" rel="stylesheet">
<style>
  :root {
    --page-bg: #e4e4e4;
    --label-white: #f4f3ee;
    --sun-yellow: #f0d83a;
    --berry-pink: #e01a6e;
    --deep-magenta: #a8197c;
    --plum: #5a1a72;
    --ink-light: #eeeeee;
    --brand-ink: #7a1c2c;
    --icon-fill: rgba(238, 238, 238, 0.2);
  }
  * { margin: 0; padding: 0; box-sizing: border-box; }
  html, body {
    width: 1200px; height: 1200px; overflow: hidden;
    background: var(--page-bg);
  }
  .canvas {
    width: 1200px; height: 1200px;
    display: flex; align-items: center; justify-content: center;
  }
  .can-label {
    position: relative;
    width: 720px; height: 1020px;
    overflow: hidden;
    background: var(--label-white);
  }
  .label-wash {
    position: absolute; inset: 0;
    background: linear-gradient(180deg,
      var(--label-white) 0%,
      var(--label-white) 16%,
      var(--sun-yellow) 36%,
      var(--berry-pink) 60%,
      var(--deep-magenta) 80%,
      var(--plum) 100%);
  }
  .brand-name {
    position: absolute; top: 128px; left: 0; right: 0;
    text-align: center;
    font-family: "Poppins", sans-serif; font-weight: 500;
    font-size: 44px; letter-spacing: 1px; line-height: 1;
    color: var(--brand-ink);
  }
  .flavour-name {
    position: absolute; top: 340px; left: 0; right: 0;
    text-align: center;
    font-family: "Sacramento", cursive;
    font-size: 160px; line-height: 1;
    color: transparent;
    -webkit-text-stroke: 1.5px var(--ink-light);
  }
  .flavour-artwork {
    position: absolute; top: 575px; left: 50%;
    width: 180px; height: 200px; margin-left: -90px;
  }
  .product-type {
    position: absolute; top: 820px; left: 0; right: 0;
    text-align: center;
    font-family: "Poppins", sans-serif; font-weight: 400;
    font-size: 30px; letter-spacing: 6px; line-height: 1;
    color: var(--ink-light);
  }
  .volume, .strength {
    position: absolute; bottom: 40px;
    font-family: "Poppins", sans-serif; font-weight: 400;
    font-size: 24px; line-height: 1; color: var(--ink-light);
  }
  .volume { left: 36px; }
  .strength { right: 36px; letter-spacing: 1px; }
</style>
</head>
<body>
  <main class="canvas">
    <section class="can-label">
      <div class="label-wash" role="img" aria-label="Soft gradient wash in yellow, pink and purple tones"></div>
      <div class="brand-name">Carrow Beacon</div>
      <div class="flavour-name">Raspberry</div>
      <svg class="flavour-artwork" viewBox="0 0 180 200" role="img" aria-label="Line illustration of a raspberry">
        <rect x="0" y="0" width="180" height="200" rx="24" fill="var(--icon-fill)"/>
      </svg>
      <div class="product-type">VODKA SODA</div>
      <div class="volume">250ml</div>
      <div class="strength">3.5% ALC/VOL</div>
    </section>
  </main>
</body>
</html>
```